Truck wrap color swap and updating

Please try different colors on the truck.
1. swap the white with pink
2. change the black to yellow and red to pink
3. change the top to yellow and the bottom to red
4. any other color combinations.

Please avoid using blue and red together. We are looking for colors to own in HVAC in the chicagoland area

Target Market(s)

married homeowners in the upper 20% income range

Industry/Entity Type

Heating and Air Conditioning

Requirements
Must have
• meet the descriptions above
Nice to have
• color variations that are NOT red and blue
Should not have
• red and blue used together

```html
<!DOCTYPE html>
<html lang="en">
<head>
<meta charset="utf-8">
<title>Marlow Heating &amp; Cooling – Truck Wrap Panels</title>
<link href="https://fonts.googleapis.com/css2?family=Archivo+Black&family=Open+Sans:wght@400&display=swap" rel="stylesheet">
<style>
  :root {
    --wrap-pink: #ec008c;
    --wrap-pink-glow: #f58fc6;
    --wrap-orange: #f8b044;
    --wrap-orange-glow: #fde0b0;
    --wrap-white: #ffffff;
    --brand-red: #c8151b;
    --label-ink: #1a1a1a;
    --mascot-dark: #3a3a3a;
    --mascot-pink: #e2237f;
  }
  html, body {
    margin: 0;
    padding: 0;
    width: 1200px;
    height: 1200px;
    overflow: hidden;
    background: var(--wrap-white);
  }
  .sheet {
    position: relative;
    width: 1200px;
    height: 1200px;
  }
  .panel-label {
    position: absolute;
    left: 14px;
    margin: 0;
    font-family: "Open Sans", sans-serif;
    font-weight: 400;
    font-size: 20px;
    color: var(--label-ink);
    line-height: 1;
  }
  .panel {
    position: absolute;
    left: 12px;
    display: block;
  }
  .panel--back { top: 51px; width: 367px; height: 325px; }
  .panel--side { width: 1181px; height: 321px; }
  .panel--right { top: 449px; }
  .panel--left { top: 856px; }

  .brand-name,
  .brand-tagline,
  .contact-phone,
  .contact-web {
    position: absolute;
    margin: 0;
    transform: translateX(-50%);
    white-space: nowrap;
    text-align: center;
    line-height: 1;
    font-family: "Archivo Black", sans-serif;
  }
  .brand-name { color: var(--brand-red); }
  .brand-tagline { color: var(--brand-red); }
  .contact-phone {
    color: var(--brand-red);
    font-size: 28px;
  }
  .contact-web {
    color: var(--label-ink);
    font-size: 11px;
    letter-spacing: 5px;
  }
  .back-brand .brand-name { left: 272px; top: 156px; font-size: 34px; }
  .back-brand .brand-tagline { left: 272px; top: 202px; font-size: 13px; }
  .right-brand .brand-name { left: 212px; top: 512px; font-size: 46px; }
  .right-brand .brand-tagline { left: 212px; top: 574px; font-size: 19px; }
  .right-brand .contact-phone { left: 202px; top: 626px; }
  .right-brand .contact-web { left: 202px; top: 660px; }
  .left-brand .brand-name { left: 984px; top: 920px; font-size: 46px; }
  .left-brand .brand-tagline { left: 984px; top: 982px; font-size: 19px; }
  .left-brand .contact-phone { left: 1003px; top: 1034px; }
  .left-brand .contact-web { left: 1003px; top: 1068px; }
</style>
</head>
<body>
<main class="sheet">

  <h2 class="panel-label" style="top:26px;">BACK</h2>
  <svg class="panel panel--back" viewBox="0 0 591 523" preserveAspectRatio="none">
    <defs>
      <radialGradient id="back-pink-glow" cx="0.6" cy="0.35" r="0.7">
        <stop offset="0" stop-color="var(--wrap-pink-glow)"/>
        <stop offset="1" stop-color="var(--wrap-pink)"/>
      </radialGradient>
      <radialGradient id="back-orange-glow" cx="0.5" cy="0.45" r="0.7">
        <stop offset="0" stop-color="var(--wrap-orange-glow)"/>
        <stop offset="1" stop-color="var(--wrap-orange)"/>
      </radialGradient>
      <linearGradient id="mascot-fill" x1="0" y1="0" x2="0" y2="1">
        <stop offset="0" stop-color="var(--mascot-dark)"/>
        <stop offset="1" stop-color="var(--mascot-pink)"/>
      </linearGradient>
    </defs>
    <rect class="wrap-base" width="591" height="523" fill="url(#back-pink-glow)"/>
    <path class="wrap-white-band" fill="var(--wrap-white)" d="M0,92 C110,35 250,15 310,38 C335,60 290,140 335,140 C420,140 500,65 591,72 L591,523 L0,523 Z"/>
    <path class="wrap-orange-wave" fill="url(#back-orange-glow)" d="M0,195 C80,160 180,112 230,120 C255,130 240,162 262,166 L500,150 C555,150 578,172 591,196 L591,523 L0,523 Z"/>
    <rect class="mascot-area" x="21" y="183" width="225" height="325" rx="36" fill="url(#mascot-fill)" role="img" aria-label="Mascot illustration: cheerful dog in a pink company shirt giving a thumbs up while carrying a duct fan on its shoulder"/>
  </svg>
  <div class="back-brand">
    <p class="brand-name">MARLOW</p>
    <p class="brand-tagline">HEATING &amp; COOLING</p>
  </div>

  <h2 class="panel-label" style="top:422px;">RIGHT</h2>
  <svg class="panel panel--side panel--right" viewBox="0 0 1902 517" preserveAspectRatio="none">
    <defs>
      <radialGradient id="right-pink-glow" cx="0.3" cy="0.15" r="0.45">
        <stop offset="0" stop-color="var(--wrap-pink-glow)"/>
        <stop offset="1" stop-color="var(--wrap-pink)"/>
      </radialGradient>
      <radialGradient id="right-orange-glow" cx="0.45" cy="0.35" r="0.7">
        <stop offset="0" stop-color="var(--wrap-orange-glow)"/>
        <stop offset="1" stop-color="var(--wrap-orange)"/>
      </radialGradient>
      <linearGradient id="right-mascot-fill" x1="0" y1="0" x2="0" y2="1">
        <stop offset="0" stop-color="var(--mascot-dark)"/>
        <stop offset="1" stop-color="var(--mascot-pink)"/>
      </linearGradient>
    </defs>
    <rect class="wrap-base" width="1902" height="517" fill="url(#right-pink-glow)"/>
    <path class="wrap-white-band" fill="var(--wrap-white)" d="M0,22 C150,160 300,195 520,195 C860,195 1100,300 1128,517 L0,517 Z"/>
    <path class="wrap-orange-wave" fill="url(#right-orange-glow)" d="M0,105 C150,200 300,232 510,232 C810,232 1020,300 1072,517 L0,517 Z"/>
    <rect class="mascot-area" x="540" y="77" width="320" height="330" rx="40" fill="url(#right-mascot-fill)" role="img" aria-label="Mascot illustration: cheerful dog in a pink company shirt giving a thumbs up while carrying a duct fan on its shoulder"/>
  </svg>
  <div class="right-brand">
    <p class="brand-name">MARLOW</p>
    <p class="brand-tagline">HEATING &amp; COOLING</p>
    <p class="contact-phone">630 555-0147</p>
    <p class="contact-web">www.marlowmech.com</p>
  </div>

  <h2 class="panel-label" style="top:829px;">LEFT</h2>
  <svg class="panel panel--side panel--left" viewBox="0 0 1902 517" preserveAspectRatio="none">
    <defs>
      <radialGradient id="left-pink-glow" cx="0.7" cy="0.15" r="0.45">
        <stop offset="0" stop-color="var(--wrap-pink-glow)"/>
        <stop offset="1" stop-color="var(--wrap-pink)"/>
      </radialGradient>
      <radialGradient id="left-orange-glow" cx="0.55" cy="0.35" r="0.7">
        <stop offset="0" stop-color="var(--wrap-orange-glow)"/>
        <stop offset="1" stop-color="var(--wrap-orange)"/>
      </radialGradient>
      <linearGradient id="left-mascot-fill" x1="0" y1="0" x2="0" y2="1">
        <stop offset="0" stop-color="var(--mascot-dark)"/>
        <stop offset="1" stop-color="var(--mascot-pink)"/>
      </linearGradient>
    </defs>
    <rect class="wrap-base" width="1902" height="517" fill="url(#left-pink-glow)"/>
    <g class="wrap-waves" transform="translate(1902,0) scale(-1,1)">
      <path class="wrap-white-band" fill="var(--wrap-white)" d="M0,22 C150,160 300,195 520,195 C860,195 1100,300 1128,517 L0,517 Z"/>
      <path class="wrap-orange-wave" fill="url(#left-orange-glow)" d="M0,105 C150,200 300,232 510,232 C810,232 1020,300 1072,517 L0,517 Z"/>
    </g>
    <rect class="mascot-area" x="1045" y="77" width="312" height="330" rx="40" fill="url(#left-mascot-fill)" role="img" aria-label="Mascot illustration: cheerful dog in a pink company shirt giving a thumbs up while carrying a duct fan on its shoulder"/>
  </svg>
  <div class="left-brand">
    <p class="brand-name">MARLOW</p>
    <p class="brand-tagline">HEATING &amp; COOLING</p>
    <p class="contact-phone">630 555-0147</p>
    <p class="contact-web">www.marlowmech.com</p>
  </div>

</main>
</body>
</html>
```